Harwell Church Yuletide Recital 2013

Create a 18x22 inch poster for an upcoming church concert event with the following details:
Theme: Jesus Is Coming Again
Date:12/21/13 Time: 10:40am
Featuring the Choirs of the Harwell Church and special guests.
Harwell FGB Church
415-36 92nd Terrace,
Laurelton, NY 10987
Pastor Desmond K. Halloway
The target audience is predominantly african-american
The concert theme has been changed to: "Jesus The Light of the World"
Church

```html
<!DOCTYPE html>
<html lang="en">
<head>
<meta charset="utf-8">
<title>Jesus the Light of the World – Harwell FGB Church</title>
<link rel="stylesheet" href="https://fonts.googleapis.com/css2?family=Audiowide&family=Ubuntu:wght@700&display=swap">
<style>
  :root {
    --page-bg: #e4e4e4;
    --sky-deep: #2f6fbe;
    --sky-mid: #5b95d6;
    --sky-light: #a9cbef;
    --cloud: #f4f8fd;
    --glow: #ffffff;
    --title-rust: #b4472a;
    --ink: #111418;
  }
  * { margin: 0; padding: 0; box-sizing: border-box; }
  html, body {
    width: 900px;
    height: 1200px;
    overflow: hidden;
    background: var(--page-bg);
  }
  .poster {
    position: absolute;
    left: 0;
    top: 50px;
    width: 900px;
    height: 1100px;
    overflow: hidden;
  }
  .poster__sky {
    position: absolute;
    inset: 0;
    background:
      radial-gradient(ellipse 38% 30% at 50% 36%, var(--glow) 0%, rgba(255,255,255,0.75) 35%, rgba(255,255,255,0) 100%),
      radial-gradient(ellipse 30% 45% at 50% 85%, rgba(255,255,255,0.95) 0%, rgba(255,255,255,0) 100%),
      radial-gradient(ellipse 30% 28% at 0% 15%, var(--cloud) 0%, rgba(244,248,253,0) 100%),
      radial-gradient(ellipse 28% 30% at 100% 12%, var(--cloud) 0%, rgba(244,248,253,0) 100%),
      radial-gradient(ellipse 30% 40% at 0% 60%, var(--cloud) 0%, rgba(244,248,253,0) 100%),
      radial-gradient(ellipse 30% 40% at 100% 60%, var(--cloud) 0%, rgba(244,248,253,0) 100%),
      radial-gradient(ellipse 70% 25% at 50% 100%, var(--cloud) 0%, rgba(244,248,253,0) 100%),
      linear-gradient(180deg, var(--sky-deep) 0%, var(--sky-mid) 40%, var(--sky-light) 75%, var(--cloud) 100%);
  }
  .poster__text {
    position: absolute;
    left: 0;
    width: 100%;
    text-align: center;
    white-space: nowrap;
  }
  .title {
    top: 208px;
    font-family: "Audiowide", sans-serif;
    font-size: 150px;
    line-height: 1;
    color: var(--title-rust);
    letter-spacing: 2px;
  }
  .subtitle {
    top: 382px;
    font-family: "Audiowide", sans-serif;
    font-size: 38px;
    line-height: 1;
    color: var(--title-rust);
    letter-spacing: 1px;
  }
  .event-detail {
    font-family: "Ubuntu", sans-serif;
    font-weight: 700;
    font-size: 30px;
    line-height: 1;
    color: var(--title-rust);
  }
  .event-detail--date { top: 453px; }
  .event-detail--time { top: 497px; }
  .venue {
    top: 912px;
    font-family: "Ubuntu", sans-serif;
    font-weight: 700;
    font-size: 33px;
    line-height: 1;
    color: var(--ink);
  }
  .venue-info {
    font-family: "Ubuntu", sans-serif;
    font-weight: 700;
    font-size: 21px;
    line-height: 1;
    color: var(--ink);
  }
  .venue-info--address { top: 952px; }
  .venue-info--pastor { top: 982px; }
  .feature-line {
    top: 1039px;
    font-family: "Ubuntu", sans-serif;
    font-weight: 700;
    font-size: 24px;
    line-height: 1;
    color: var(--ink);
  }
</style>
</head>
<body>
  <main class="poster">
    <div class="poster__sky" role="img" aria-label="Bright blue sky framed by white clouds, with light rays and a stairway rising into the glow"></div>

    <h1 class="poster__text title">Jesus</h1>
    <p class="poster__text subtitle">the Light of the World</p>

    <p class="poster__text event-detail event-detail--date">Date:12/21/13</p>
    <p class="poster__text event-detail event-detail--time">Time: 10:40am</p>

    <h2 class="poster__text venue">Harwell FGB Church</h2>
    <p class="poster__text venue-info venue-info--address">415-36 92nd Terrace, Laurelton, NY 10987</p>
    <p class="poster__text venue-info venue-info--pastor">Pastor Desmond K. Halloway</p>

    <p class="poster__text feature-line">Featuring the Choirs of the Harwell Church and special guests.</p>
  </main>
</body>
</html>
```